Falcrest security business card

Looking for a business card for my security company

Target Market(s)

Security

Industry/Entity Type

Security

Contact Information for Business Card

Name - Gil Marston. Title - General manager - direct 314 862.4490 website www. falcrestsecurityservices.example email - gil@ falcrestsecurityservices.example

Requirements
Must have
• Logo attached

```html
<!DOCTYPE html>
<html lang="en">
<head>
<meta charset="utf-8">
<title>Falcrest Security Services – Business Card</title>
<link rel="stylesheet" href="https://fonts.googleapis.com/css2?family=Saira:wght@400;500;700&display=swap">
<style>
  :root {
    --stage: #2a2a2c;
    --card-dark: #1c1d1f;
    --gold: #cfa548;
    --gold-light: #ecd48f;
    --gold-deep: #b3832c;
    --ink: #111111;
    --rule: #6b6b6b;
  }
  * { margin: 0; padding: 0; box-sizing: border-box; }
  html, body {
    width: 1200px; height: 1108px; overflow: hidden;
    background: var(--stage);
    font-family: "Saira", sans-serif;
  }
  .stage {
    position: relative; width: 1200px; height: 1108px;
    display: flex; justify-content: center; align-items: center; gap: 60px;
  }
  .card {
    width: 430px; height: 740px; border-radius: 22px;
    position: relative; overflow: hidden;
    box-shadow: 0 18px 40px rgba(0,0,0,.45);
  }
  .card-front {
    background: var(--card-dark);
    color: var(--gold);
    display: flex; flex-direction: column; align-items: center;
    text-align: center;
  }
  .brand {
    margin-top: 150px;
    display: flex; align-items: center; gap: 14px;
  }
  .brand-mark {
    width: 14px; height: 14px; background: var(--gold);
  }
  .brand-name {
    font-size: 56px; font-weight: 500; letter-spacing: 1px;
    color: var(--gold); text-transform: uppercase; line-height: 1;
  }
  .person { margin-top: 230px; }
  .person-name {
    font-size: 30px; font-weight: 700; text-transform: uppercase; letter-spacing: 1px;
  }
  .person-title {
    font-size: 18px; font-weight: 400; text-transform: uppercase; margin-top: 2px;
  }
  .icon-row {
    margin-top: 20px; display: flex; align-items: center; gap: 8px;
  }
  .icon-row .rule { width: 80px; height: 1px; background: var(--rule); }
  .icon {
    width: 30px; height: 30px; border-radius: 5px;
    background: linear-gradient(135deg, var(--gold-light), var(--gold-deep));
    display: flex; align-items: center; justify-content: center;
  }
  .icon svg { width: 18px; height: 18px; }
  .contact { margin-top: 14px; line-height: 1.3; }
  .contact-phone { font-size: 26px; font-weight: 500; }
  .contact-line { font-size: 17px; font-weight: 400; text-transform: uppercase; letter-spacing: .2px; }

  .card-back {
    background: linear-gradient(200deg, var(--gold-light) 0%, var(--gold) 45%, var(--gold-deep) 100%);
  }
  .emboss-pattern {
    position: absolute; inset: 0;
    background: linear-gradient(200deg, rgba(255,255,255,.12), rgba(0,0,0,.06));
  }
  .back-brand {
    position: absolute; left: 0; right: 0; bottom: 150px;
    display: flex; justify-content: center; align-items: center; gap: 10px;
  }
  .back-brand .brand-mark { width: 10px; height: 10px; background: var(--ink); }
  .back-brand .brand-name { font-size: 36px; color: var(--ink); }
</style>
</head>
<body>
<main class="stage">
  <section class="card card-front" aria-label="Card front">
    <div class="brand">
      <span class="brand-mark"></span>
      <span class="brand-name">Falcrest</span>
    </div>
    <div class="person">
      <p class="person-name">Gil Marston</p>
      <p class="person-title">General Manager</p>
    </div>
    <div class="icon-row">
      <span class="rule"></span>
      <span class="icon" aria-label="Phone">
        <svg viewBox="0 0 24 24"><path fill="#1c1d1f" d="M6.6 10.8a15 15 0 0 0 6.6 6.6l2.2-2.2a1 1 0 0 1 1-.25 11.4 11.4 0 0 0 3.6.57 1 1 0 0 1 1 1V20a1 1 0 0 1-1 1A17 17 0 0 1 3 4a1 1 0 0 1 1-1h3.5a1 1 0 0 1 1 1c0 1.25.2 2.45.57 3.6a1 1 0 0 1-.25 1z"/></svg>
      </span>
      <span class="icon" aria-label="Email">
        <svg viewBox="0 0 24 24"><rect x="3" y="6" width="18" height="12" fill="none" stroke="#1c1d1f" stroke-width="2"/><path d="M3 6l9 7 9-7M3 18l7-6M21 18l-7-6" fill="none" stroke="#1c1d1f" stroke-width="1.6"/></svg>
      </span>
      <span class="icon" aria-label="Website">
        <svg viewBox="0 0 24 24"><circle cx="12" cy="12" r="8" fill="none" stroke="#1c1d1f" stroke-width="2"/><path d="M4 12h16M12 4c3 3 3 13 0 16M12 4c-3 3-3 13 0 16" fill="none" stroke="#1c1d1f" stroke-width="1.4"/></svg>
      </span>
      <span class="rule"></span>
    </div>
    <div class="contact">
      <p class="contact-phone">314 862.4490</p>
      <p class="contact-line">gil@ falcrestsecurityservices.example</p>
      <p class="contact-line">www. falcrestsecurityservices.example</p>
    </div>
  </section>

  <section class="card card-back" aria-label="Card back">
    <div class="emboss-pattern" role="img" aria-label="Repeating embossed brand pattern in tone-on-tone gold"></div>
    <div class="back-brand">
      <span class="brand-mark"></span>
      <span class="brand-name">Falcrest</span>
    </div>
  </section>
</main>
</body>
</html>
```